Design a Unique and Eye-Catching Necklace Card for Wendaray's New Brightwell Line

Attention all creative minds from around the world! Wendaray, a company known for its free-spirited and bohemian chic vibe, is proud to announce a new design contest. We are inviting you to create a dynamic and unique necklace card for our upcoming Brightwell line.

Our new Brightwell line comprises 12-20 unique necklace combinations. Each necklace features different stones, each with its own healing properties and associated zodiac sign. We are looking for a template that can be easily modified to change the names of the stones, zodiac sign, and the colors to match the specific stones on each necklace.

The card should be 3 x 4,
It should include the names of the stones, the associated zodiac sign (if applicable), a few words about the healing properties of the stones, and a captivating graphic that represents the colors of the stones.

Our goal is to delight our customers with packaging as unique as the necklaces themselves. The necklace should be the focal point, but the text and graphic on the card should also draw the eye.

Please note that our target audience includes mid-priced boutiques across the country and festival-goers in Colorado. Your design should reflect the unique taste and free spirit of our clientele.

We are excited to see your creativity shine in this project. If there are any points that need clarification, please do not hesitate to ask. We look forward to your participation in bringing the Brightwell line to life!
https://www.draftnook.example/board/KQ7mPzR2tLw/edit

https://www.draftnook.example/board/VJ3nHsX8qYb/edit
I want to use the flowing watercolor and have it change with each necklace color.
Use the necklaces below. Incorporate the zodiac symbol as is shown below.

Examples of other cards in our collection

The Little Pebble Pendant: https://www.draftnook.example/board/TB5wGdM4cRu/edit

Other examples of necklace cards I like:

https://www.craftbazaro.example/item/731905284/green-stone-pendant

https://www.craftbazaro.example/item/462918037/birthstone-pendant-green

https://www.craftbazaro.example/item/2907315628/crystal-bead-bracelets

https://www.craftbazaro.example/item/3816402795/dark-stone-guard-pendant

Target Market(s)

Women aged 25-50 with a spiritual, hippy, bohemain, yoga vibe.

Industry/Entity Type

Handmade Jewelry | Wholesale jewelry | Retail Jewelry sales at Festivals

Font styles to use
Script

Colors

Designer to choose colors to be used in the design.

Requirements
Must have
• A template that can be interchangable with the stone colors, names and healing properties.
Nice to have
• Some different ideas about the graphic color patterns on the card.
Should not have
• Any graphic that would cover the middle of the necklace card and keep people from seeing the neckalce

```html
<!DOCTYPE html>
<html lang="en">
<head>
<meta charset="utf-8">
<title>Wendaray Brightwell Necklace Cards</title>
<link href="https://fonts.googleapis.com/css2?family=Allura&family=PT+Sans&display=swap" rel="stylesheet">
<style>
  :root {
    --sheet: #ffffff;
    --fluorite-top: #8456ad; --fluorite-mid: #f6eef6; --fluorite-bottom: #9a63b5; --fluorite-ink: #6a2a92; --fluorite-wash: #9867b8;
    --turq-top: #3eb4b2; --turq-mid: #eef9f8; --turq-bottom: #5cbfbb; --turq-ink: #16706d; --turq-wash: #4aaeab;
    --kyan-top: #2f3f9c; --kyan-mid: #f4f4fb; --kyan-low: #8cbcf0; --kyan-bottom: #6d6fc6; --kyan-ink: #3862ae; --kyan-wash: #7474c8;
    --amaz-top: #4d84d5; --amaz-mid: #f3f6fd; --amaz-low: #a3cbf1; --amaz-bottom: #7b86d2; --amaz-ink: #2f5aa8; --amaz-wash: #7c8ad4;
  }
  * { margin: 0; padding: 0; box-sizing: border-box; }
  html, body { width: 1200px; height: 1065px; overflow: hidden; background: var(--sheet); }
  .sheet { position: relative; width: 1200px; height: 1065px; }
  .defs { position: absolute; width: 0; height: 0; }
  .card { position: absolute; width: 388px; height: 518px; overflow: hidden; }
  .card--fluorite { background: linear-gradient(180deg, var(--fluorite-top) 0%, #c9a6d4 30%, var(--fluorite-mid) 55%, #d6bade 75%, var(--fluorite-bottom) 100%); }
  .card--turquoise { background: linear-gradient(180deg, var(--turq-top) 0%, #a9dedc 32%, var(--turq-mid) 55%, #a5dcd9 75%, var(--turq-bottom) 100%); }
  .card--kyanite { background: linear-gradient(180deg, var(--kyan-top) 0%, #a6a9dc 30%, var(--kyan-mid) 58%, var(--kyan-low) 78%, var(--kyan-bottom) 100%); }
  .card--amazonite { background: linear-gradient(180deg, var(--amaz-top) 0%, #b6c6ee 32%, var(--amaz-mid) 55%, var(--amaz-low) 75%, var(--amaz-bottom) 100%); }
  .pos-1 { left: 7px; top: 10px; }
  .pos-2 { left: 405px; top: 10px; }
  .pos-3 { left: 803px; top: 10px; }
  .pos-4 { left: 7px; top: 537px; }
  .pos-5 { left: 405px; top: 537px; }
  .pos-6 { left: 803px; top: 537px; }
  .art { position: absolute; inset: 0; width: 388px; height: 518px; }
  .stone-name { font-family: "Allura", cursive; font-weight: 400; }
  .sparkle { fill: none; stroke: #ffffff; stroke-width: 1.6; }
  .property { position: absolute; left: 0; width: 100%; text-align: center; font-family: "PT Sans", sans-serif; font-size: 12px; line-height: 14px; }
  .ink-fluorite { color: var(--fluorite-ink); fill: var(--fluorite-ink); }
  .ink-turq { color: var(--turq-ink); fill: var(--turq-ink); }
  .ink-kyan { color: var(--kyan-ink); fill: var(--kyan-ink); }
  .ink-amaz { color: var(--amaz-ink); fill: var(--amaz-ink); }
</style>
</head>
<body>
<main class="sheet">
  <svg class="defs" aria-hidden="true">
    <defs>
      <filter id="wash-soft" x="-10%" y="-20%" width="120%" height="140%"><feGaussianBlur stdDeviation="3"/></filter>
      <filter id="zodiac-soft" x="-30%" y="-30%" width="160%" height="160%"><feGaussianBlur stdDeviation="10"/></filter>
    </defs>
  </svg>

  <!-- Fluorite -->
  <section class="card card--fluorite pos-1">
    <svg class="art" viewBox="0 0 388 518">
      <defs>
        <linearGradient id="fluoriteBeads" x1="0" x2="1">
          <stop offset="0" stop-color="#ece6da"/><stop offset="0.35" stop-color="#8f5aa6"/>
          <stop offset="0.55" stop-color="#4a2a7a"/><stop offset="0.8" stop-color="#7aaea5"/><stop offset="1" stop-color="#b9ccc4"/>
        </linearGradient>
      </defs>
      <g role="img" aria-label="Violet watercolour wash">
        <path d="M20 0 H388 V40 C350 70 320 55 280 78 C240 100 200 132 160 120 C130 110 110 80 70 78 C40 76 30 90 20 70 Z" fill="var(--fluorite-wash)" opacity="0.55" filter="url(#wash-soft)"/>
        <path d="M60 518 C55 480 80 440 120 432 C160 424 190 408 230 412 C280 416 320 440 360 470 L388 500 V518 Z" fill="var(--fluorite-wash)" opacity="0.55" filter="url(#wash-soft)"/>
        <circle cx="128" cy="75" r="3" fill="var(--fluorite-wash)" opacity="0.6"/>
        <circle cx="38" cy="373" r="2.5" fill="var(--fluorite-wash)" opacity="0.5"/>
      </g>
      <ellipse cx="195" cy="285" rx="70" ry="75" fill="#e2d6f0" opacity="0.6" filter="url(#zodiac-soft)" role="img" aria-label="Faint Pisces twin fish illustration"/>
      <path d="M0 228 Q200 330 388 232" fill="none" stroke="#d8d8d8" stroke-width="1"/>
      <path d="M44 248 Q205 322 359 236" fill="none" stroke="url(#fluoriteBeads)" stroke-width="18" stroke-linecap="round" role="img" aria-label="Photo of faceted fluorite bead necklace"/>
      <text class="stone-name ink-fluorite" x="104" y="190" font-size="48"><tspan font-size="82">F</tspan>luorite</text>
    </svg>
    <p class="property ink-fluorite" style="top:385px;">Impoves Decision Making</p>
  </section>

  <!-- Turquoise with necklace -->
  <section class="card card--turquoise pos-2">
    <svg class="art" viewBox="0 0 388 518">
      <defs>
        <linearGradient id="turqBeads" x1="0" x2="1">
          <stop offset="0" stop-color="#6d5a48"/><stop offset="0.3" stop-color="#3e9a8e"/>
          <stop offset="0.5" stop-color="#9bc07a"/><stop offset="0.75" stop-color="#d0632a"/><stop offset="1" stop-color="#5e3a28"/>
        </linearGradient>
      </defs>
      <g role="img" aria-label="Teal watercolour wash">
        <path d="M0 0 H388 V30 C360 50 320 40 300 80 C280 110 250 140 210 130 C170 120 130 100 100 90 C70 80 40 80 20 60 L0 50 Z" fill="var(--turq-wash)" opacity="0.55" filter="url(#wash-soft)"/>
        <path d="M60 518 C60 470 80 440 120 430 C170 400 220 390 260 405 C300 420 330 440 388 450 V518 Z" fill="var(--turq-wash)" opacity="0.55" filter="url(#wash-soft)"/>
        <circle cx="50" cy="451" r="7" fill="var(--turq-wash)" opacity="0.7"/>
        <circle cx="28" cy="423" r="3" fill="var(--turq-wash)" opacity="0.6"/>
      </g>
      <path d="M0 95 C30 300 90 330 194 330 C300 330 360 300 388 80" fill="none" stroke="#d8d8d8" stroke-width="1"/>
      <path d="M22 155 C45 295 110 316 194 316 C290 316 345 290 360 155" fill="none" stroke="url(#turqBeads)" stroke-width="22" stroke-linecap="round" role="img" aria-label="Photo of square turquoise bead necklace"/>
      <text class="stone-name ink-turq" x="120" y="212" font-size="40"><tspan font-size="76">T</tspan>urquoise</text>
    </svg>
    <p class="property ink-turq" style="top:343px;">Helpful for CLarity and Self Experssion</p>
  </section>

  <!-- Aquamarine Kyanite zodiac -->
  <section class="card card--kyanite pos-3">
    <svg class="art" viewBox="0 0 388 518">
      <g role="img" aria-label="Indigo watercolour wash">
        <path d="M30 0 H388 V40 C350 60 320 50 290 70 C260 90 220 95 180 92 C140 88 110 70 90 40 C70 20 40 20 30 0 Z" fill="var(--kyan-wash)" opacity="0.55" filter="url(#wash-soft)"/>
        <path d="M10 518 C30 470 70 450 130 455 C160 420 210 400 260 420 C300 440 340 450 388 430 V518 Z" fill="var(--kyan-wash)" opacity="0.55" filter="url(#wash-soft)"/>
        <circle cx="348" cy="478" r="7" fill="var(--kyan-wash)" opacity="0.7"/>
      </g>
      <ellipse cx="195" cy="285" rx="75" ry="80" fill="#c9d3f4" opacity="0.65" filter="url(#zodiac-soft)" role="img" aria-label="Pisces twin fish illustration in blue line work"/>
      <path class="sparkle" d="M126 128 V144 M118 136 H134"/>
      <text class="stone-name ink-kyan" x="129" y="149" font-size="40"><tspan font-size="86">A</tspan>quamaine</text>
      <text class="stone-name ink-kyan" x="90" y="197" font-size="36"><tspan font-size="72">K</tspan>yanite</text>
    </svg>
    <p class="property ink-kyan" style="top:383px;">Reduce Stress amd Anxiety</p>
  </section>

  <!-- Turquoise Amazonite -->
  <section class="card card--amazonite pos-4">
    <svg class="art" viewBox="0 0 388 518">
      <defs>
        <linearGradient id="amazBeads" x1="0" x2="1">
          <stop offset="0" stop-color="#7cc3c4"/><stop offset="0.3" stop-color="#e6c58f"/>
          <stop offset="0.5" stop-color="#8b7a4f"/><stop offset="0.75" stop-color="#f0d28e"/><stop offset="1" stop-color="#6fc3a2"/>
        </linearGradient>
      </defs>
      <g role="img" aria-label="Blue watercolour wash">
        <path d="M0 0 H388 V40 C350 60 320 70 280 95 C240 115 190 110 160 100 C130 90 100 100 70 90 C40 80 20 50 0 40 Z" fill="var(--amaz-wash)" opacity="0.55" filter="url(#wash-soft)"/>
        <path d="M0 518 V470 C40 450 90 430 140 440 C170 400 220 390 260 410 C300 420 340 440 388 430 V518 Z" fill="var(--amaz-wash)" opacity="0.55" filter="url(#wash-soft)"/>
        <circle cx="360" cy="418" r="7" fill="var(--amaz-wash)" opacity="0.7"/>
        <circle cx="62" cy="440" r="6" fill="var(--amaz-wash)" opacity="0.6"/>
      </g>
      <path d="M0 212 Q194 318 388 218" fill="none" stroke="#d8d8d8" stroke-width="1"/>
      <path d="M28 230 Q194 320 358 240" fill="none" stroke="url(#amazBeads)" stroke-width="18" stroke-linecap="round" role="img" aria-label="Photo of turquoise and amazonite bead necklace"/>
      <path class="sparkle" d="M168 166 V182 M160 174 H176"/>
      <text class="stone-name ink-amaz" x="156" y="177" font-size="38"><tspan font-size="76">T</tspan>urquoise</text>
      <text class="stone-name ink-amaz" x="102" y="207" font-size="38"><tspan font-size="86">A</tspan>mazonite</text>
    </svg>
    <p class="property ink-amaz" style="top:338px;">Sheilds from Electromagnetic pollution</p>
  </section>

  <!-- Aquamarine Kyanite with necklace -->
  <section class="card card--kyanite pos-5">
    <svg class="art" viewBox="0 0 388 518">
      <defs>
        <linearGradient id="kyanBeads" x1="0" x2="1">
          <stop offset="0" stop-color="#3d63b5"/><stop offset="0.35" stop-color="#8eb2df"/>
          <stop offset="0.5" stop-color="#cfe0f2"/><stop offset="0.7" stop-color="#4a74c2"/><stop offset="1" stop-color="#2e55a8"/>
        </linearGradient>
      </defs>
      <g role="img" aria-label="Indigo watercolour wash">
        <path d="M30 0 H388 V40 C350 60 320 50 290 70 C260 90 220 95 180 92 C140 88 110 70 90 40 C70 20 40 20 30 0 Z" fill="var(--kyan-wash)" opacity="0.55" filter="url(#wash-soft)"/>
        <path d="M10 518 C30 470 70 450 130 455 C160 420 210 400 260 420 C300 440 340 450 388 430 V518 Z" fill="var(--kyan-wash)" opacity="0.55" filter="url(#wash-soft)"/>
        <circle cx="342" cy="478" r="7" fill="var(--kyan-wash)" opacity="0.7"/>
      </g>
      <ellipse cx="200" cy="300" rx="75" ry="85" fill="#c9d5f4" opacity="0.65" filter="url(#zodiac-soft)" role="img" aria-label="Pisces twin fish illustration in blue line work"/>
      <path d="M0 212 Q194 318 388 200" fill="none" stroke="#d8d8d8" stroke-width="1"/>
      <path d="M30 228 Q190 320 334 234" fill="none" stroke="url(#kyanBeads)" stroke-width="20" stroke-linecap="round" role="img" aria-label="Photo of kyanite and aquamarine bead necklace"/>
      <path class="sparkle" d="M124 127 V143 M116 135 H132"/>
      <text class="stone-name ink-kyan" x="129" y="149" font-size="40"><tspan font-size="86">A</tspan>quamaine</text>
      <text class="stone-name ink-kyan" x="90" y="197" font-size="36"><tspan font-size="72">K</tspan>yanite</text>
    </svg>
    <p class="property ink-kyan" style="top:384px;">Reduce Stress amd Anxiety</p>
  </section>

  <!-- Turquoise blank -->
  <section class="card card--turquoise pos-6">
    <svg class="art" viewBox="0 0 388 518">
      <g role="img" aria-label="Teal watercolour wash">
        <path d="M0 0 H388 V30 C360 50 320 45 300 80 C280 115 250 135 210 128 C170 120 130 95 100 80 C70 65 30 75 0 60 Z" fill="var(--turq-wash)" opacity="0.55" filter="url(#wash-soft)"/>
        <path d="M40 518 C50 470 80 440 130 430 C170 400 220 395 260 410 C300 425 340 440 388 445 V518 Z" fill="var(--turq-wash)" opacity="0.55" filter="url(#wash-soft)"/>
        <circle cx="52" cy="450" r="7" fill="var(--turq-wash)" opacity="0.7"/>
      </g>
      <text class="stone-name ink-turq" x="121" y="210" font-size="40"><tspan font-size="76">T</tspan>urquoise</text>
    </svg>
    <p class="property ink-turq" style="top:346px;">Helpful for CLarity and Self Experssion</p>
  </section>

</main>
</body>
</html>
```